Kivo4 Website design (Need help to re-design our website)

We need someone to help us re-design our website and launch it. All contents for the website are ready. (Website: https://www.kivo4.com.au/)

-Rearrange categories:
1. Heat Pumps (Link to PALOX site: https://palox.com.au/)
2. Solar (Under the Solar category; remove solar panels, solar inverters, and solar batteries)
3. LED
4. Capability Statement
5. Service and Support
6. Contact us

Home page - redesign but the free quote will stay.

NOTE:
-Try using professional fonts (Example: Helvetica, etc.)
-Try to play with colours related to sustainability, eco-friendliness, solar, energy, and energy efficiency.
-The website's Footer should be readable and use light colour.

Target Market(s)

Residentials & commercial buildings

Industry/Entity Type

SOLAR ENERGY PROVIDER

Coding

Coded - Design and coding required

Colors

Designer to choose colors to be used in the design.

Requirements
Nice to have
• Effects/transition on the words/copy/images.

```html
<!DOCTYPE html>
<html lang="en">
<head>
<meta charset="utf-8">
<title>Kivo4 – Solar Energy Provider</title>
<link rel="stylesheet" href="https://fonts.googleapis.com/css2?family=Krona+One&family=Nunito+Sans:wght@400;600;700;800&family=Oswald:wght@500&display=swap">
<style>
:root{
  --blue:#1a63c4;
  --blue-deep:#164fa8;
  --blue-bright:#2185e0;
  --green:#4a9b2e;
  --green-light:#6cbd3c;
  --ink:#1b1b1b;
  --text:#4a4a4a;
  --muted:#8a8a8a;
  --band:#efefef;
  --white:#ffffff;
  --star:#f5a30a;
  --display:"Krona One", "Arial Black", sans-serif;
  --body:"Nunito Sans", Arial, sans-serif;
  --hero:"Oswald", "Arial Narrow", sans-serif;
}
*{box-sizing:border-box;margin:0;padding:0}
html,body{width:1200px;height:3866px;overflow:hidden}
body{position:relative;background:var(--white);font-family:var(--body);color:var(--text)}
svg.icon{width:16px;height:16px;fill:none;stroke:currentColor;stroke-width:2;stroke-linecap:round;stroke-linejoin:round}
.btn{position:absolute;display:flex;align-items:center;justify-content:center;gap:8px;background:var(--blue);color:var(--white);font:700 14px var(--body);border-radius:2px}
.display{font-family:var(--display);font-size:33px;letter-spacing:1px;color:var(--ink);line-height:1}
.display .accent{color:var(--blue)}

/* header */
.site-header{position:absolute;left:0;top:0;width:1200px;height:84px}
.brand{position:absolute;left:153px;top:14px;display:flex;align-items:center;gap:10px}
.brand-mark{width:28px;height:28px;border-radius:50%;background:var(--green)}
.brand-name{font:800 36px/1 var(--body);color:var(--blue)}
.brand-tag{position:absolute;left:191px;top:58px;font:600 8px var(--body);color:var(--blue-deep);white-space:nowrap}
.main-nav{position:absolute;right:130px;top:36px;display:flex;gap:37px;font:600 13px var(--body);color:var(--ink)}
.main-nav span{display:flex;align-items:center;gap:3px}

/* hero */
.hero{position:absolute;left:12px;top:84px;width:1188px;height:550px;background:linear-gradient(180deg,#5d7c98 0%,#9fb8c9 30%,#34506e 48%,#1f3552 70%,#4d6e2f 90%,#5f8a34 100%)}
.hero-title{position:absolute;left:143px;top:118px;font:500 52px/58px var(--hero);color:var(--white);letter-spacing:.5px}
.hero-sub{position:absolute;left:143px;top:236px;font:600 19px var(--body);color:var(--white)}
.hero-copy{position:absolute;left:143px;top:272px;width:400px;font:400 13px/23px var(--body);color:var(--white)}
.hero .btn{left:143px;top:361px;width:128px;height:42px}

.quote{position:absolute;left:615px;top:63px;width:443px;height:425px;background:rgba(255,255,255,.28)}
.quote-head{height:40px;background:linear-gradient(90deg,var(--blue-deep),var(--blue-bright));color:var(--white);font:700 19px/40px var(--body);text-align:center}
.field{position:absolute;height:34px;background:rgba(255,255,255,.92);display:flex;align-items:center;justify-content:space-between;padding:0 12px;font:400 12px var(--body);color:#555}
.field em{color:#d02020;font-style:normal}
.field svg{width:15px;height:15px;color:#333}
.field.message{align-items:flex-start;padding-top:10px;height:97px}
.quote .btn{left:157px;top:360px;width:128px;height:44px}

/* about */
.about-visual{position:absolute;left:175px;top:715px;width:395px;height:480px;border-radius:0 0 200px 200px;background:linear-gradient(180deg,#f4f6f8 0%,#d7e6f4 40%,#6d9fd8 75%,#2a5fa8 100%)}
.about{position:absolute;left:683px;top:808px;width:390px}
.about p{font:400 12.5px/23px var(--body);color:var(--text)}
.about h3{font:800 19px var(--body);color:var(--ink);margin:14px 0 10px}
.about .display{margin-bottom:16px}
.about .btn{position:relative;width:128px;height:44px;margin-top:22px}

/* projects */
.projects{position:absolute;left:12px;top:1283px;width:1188px;height:652px;background:var(--band)}
.projects .display{position:absolute;left:141px;top:90px}
.tab{position:absolute;top:85px;height:44px;width:155px;display:flex;align-items:center;justify-content:center;font:600 14px var(--body)}
.tab.active{left:741px;background:var(--blue);color:var(--white)}
.tab.plain{left:903px;background:var(--white);border:1px solid #333;color:var(--ink)}
.project{position:absolute;top:157px;width:215px;height:339px;display:flex;flex-direction:column;justify-content:flex-end;align-items:center;padding-bottom:12px;color:var(--white)}
.project b{font:700 17px var(--body)}
.project span{font:400 13px var(--body)}
.p1{left:141px;background:linear-gradient(180deg,#a9c4de 0%,#8d6a4c 30%,#3a4f76 60%,#9b6a45 100%)}
.p2{left:374px;background:linear-gradient(180deg,#4f89cc 0%,#9dc1e4 45%,#2f3e58 62%,#5c6b82 100%)}
.p3{left:608px;background:linear-gradient(180deg,#8fb2d8 0%,#6f7d92 30%,#47566e 70%,#8e8e8e 100%)}
.p4{left:843px;background:linear-gradient(180deg,#6f9fd6 0%,#a9c8e6 40%,#5e7390 58%,#7a9a60 80%,#8aa56a 100%)}
.progress{position:absolute;left:141px;top:543px;width:783px;height:4px;background:#111}
.progress i{display:block;width:317px;height:4px;background:var(--green)}
.circle-btn{position:absolute;width:32px;height:32px;border-radius:50%;display:flex;align-items:center;justify-content:center}
.circle-btn svg{width:14px;height:14px}

/* reviews */
.reviews-title{position:absolute;left:0;width:1200px;top:2020px;text-align:center}
.review{position:absolute;width:283px;height:230px;background:var(--white);box-shadow:0 4px 14px rgba(0,0,0,.12)}
.review p{padding:22px 18px 0;text-align:center;font:400 12.5px/23px var(--body);color:var(--text);height:172px}
.review footer{position:absolute;left:0;bottom:0;width:100%;height:58px;border-top:1px solid #e3e3e3;padding:10px 28px;display:flex;justify-content:space-between;align-items:center}
.review .who{font:600 14px var(--body);color:var(--ink)}
.stars{display:flex;gap:2px;margin-top:3px}
.stars svg{width:9px;height:9px;fill:var(--star);stroke:none}
.review .dot{width:16px;height:16px;border-radius:50%;background:#e1e1e1}
.side-arrow{position:absolute;top:2217px;width:34px;height:34px;border-radius:50%;background:var(--white);box-shadow:0 2px 8px rgba(0,0,0,.12);display:flex;align-items:center;justify-content:center;color:#aaa}
.side-arrow.dark{color:#333}

/* signup */
.signup{position:absolute;left:12px;top:2438px;width:1188px;height:650px;background:linear-gradient(180deg,#243246 0%,#2d3d50 40%,#1d2a38 75%,#27313c 100%)}
.signup .display{position:absolute;left:144px;top:174px;color:var(--white);line-height:38px}
.signup p{position:absolute;left:144px;font:400 13px var(--body);color:var(--white)}
.subscribe{position:absolute;left:144px;top:300px;width:408px;height:44px;border:1px solid var(--white);display:flex}
.subscribe .input{flex:1;display:flex;align-items:center;gap:10px;padding-left:20px;font:400 12px var(--body);color:var(--white)}
.subscribe .send{width:126px;background:var(--blue);color:var(--white);font:600 14px var(--body);display:flex;align-items:center;justify-content:center}
.signup .btn{left:144px;top:415px;width:128px;height:44px}

/* partners */
.strip{position:absolute;left:153px;width:917px;height:72px;background:var(--white);box-shadow:0 2px 10px rgba(0,0,0,.1);display:flex;align-items:center}
.strip-label{height:72px;background:linear-gradient(90deg,var(--green),var(--green-light));color:var(--white);font:700 20px var(--body);display:flex;align-items:center;justify-content:center}
.strip .chev{width:14px;height:14px;color:#333;margin:0 16px}
.strip .items{flex:1;display:flex;justify-content:space-around;align-items:center}
.client-name{font:800 15px var(--body);color:var(--blue-deep)}
.badge{width:76px;height:30px;border-radius:3px;background:#d9dee4}
.badge.round{width:40px;height:40px;border-radius:50%;background:#cfe3c4}

/* footer */
.site-footer{position:absolute;left:12px;top:3460px;width:1188px;height:406px;background:linear-gradient(180deg,var(--blue-bright) 0%,var(--blue-deep) 100%);color:var(--white)}
.site-footer .brand{left:141px;top:52px}
.site-footer .brand-name{color:var(--white);font-size:32px}
.site-footer .brand-mark{background:var(--white)}
.site-footer .brand-tag{left:178px;top:92px;color:var(--white)}
.socials{position:absolute;left:177px;top:136px;display:flex;gap:11px}
.socials span{width:32px;height:32px;border-radius:50%;background:var(--green-light)}
.col{position:absolute;top:70px}
.col h4{font:400 15px var(--display);letter-spacing:.5px;margin-bottom:16px}
.links li{list-style:none;font:400 12.5px var(--body);margin-bottom:22px;display:flex;gap:10px;align-items:center}
.links li::before{content:"›";font-size:13px}
.contact-item{display:flex;gap:12px;margin-bottom:34px}
.contact-item .ico{width:26px;height:26px;border-radius:50%;background:var(--white);color:var(--green);display:flex;align-items:center;justify-content:center;flex:none}
.contact-item .ico svg{width:14px;height:14px}
.contact-item b{font:700 14px var(--body);display:block}
.contact-item span{font:400 12.5px var(--body)}
.office{display:flex;gap:10px;margin-bottom:11px;font:400 12.5px/16px var(--body)}
.office svg{width:20px;height:20px;flex:none;fill:var(--white);stroke:var(--green)}
.legal{position:absolute;left:141px;top:372px;width:917px;display:flex;justify-content:space-between;font:400 12px var(--body)}
</style>
</head>
<body>
<svg width="0" height="0" style="position:absolute">
  <defs>
    <symbol id="i-user" viewBox="0 0 24 24"><circle cx="12" cy="8" r="4"/><path d="M4 21c1-4 4-6 8-6s7 2 8 6"/></symbol>
    <symbol id="i-phone" viewBox="0 0 24 24"><path d="M5 3h4l2 5-3 2c1 2.5 3 4.5 6 6l2-3 5 2v4c0 1-1 2-2 2C10 21 3 14 3 5c0-1 1-2 2-2z"/></symbol>
    <symbol id="i-mail" viewBox="0 0 24 24"><rect x="3" y="5" width="18" height="14" rx="1"/><path d="M3 6l9 7 9-7"/></symbol>
    <symbol id="i-pin" viewBox="0 0 24 24"><path d="M12 22s7-7 7-12a7 7 0 0 0-14 0c0 5 7 12 7 12z"/><circle cx="12" cy="10" r="2.5"/></symbol>
    <symbol id="i-down" viewBox="0 0 24 24"><path d="M7 10l5 5 5-5"/></symbol>
    <symbol id="i-left" viewBox="0 0 24 24"><path d="M15 5l-7 7 7 7"/></symbol>
    <symbol id="i-right" viewBox="0 0 24 24"><path d="M9 5l7 7-7 7"/></symbol>
    <symbol id="i-arrow-l" viewBox="0 0 24 24"><path d="M20 12H4M10 6l-6 6 6 6"/></symbol>
    <symbol id="i-arrow-r" viewBox="0 0 24 24"><path d="M4 12h16M14 6l6 6-6 6"/></symbol>
    <symbol id="i-clock" viewBox="0 0 24 24"><circle cx="12" cy="12" r="9"/><path d="M12 7v5l3 2"/></symbol>
    <symbol id="i-download" viewBox="0 0 24 24"><path d="M12 4v11M7 10l5 5 5-5M4 20h16"/></symbol>
    <symbol id="i-star" viewBox="0 0 24 24"><path d="M12 2l3 7 7 .6-5.3 4.7 1.7 7.3L12 17.8 5.6 21.6l1.7-7.3L2 9.6 9 9z"/></symbol>
  </defs>
</svg>

<header class="site-header">
  <div class="brand"><span class="brand-mark"></span><span class="brand-name">Kivo4</span></div>
  <div class="brand-tag">Clean Power Solutions For Homes &amp; Business</div>
  <nav class="main-nav">
    <span>Heat Pumps</span>
    <span>Solar <svg class="icon" style="width:11px;height:11px"><use href="#i-down"/></svg></span>
    <span>Capability Statement</span>
    <span>LED</span>
    <span>Service &amp; Support</span>
    <span>Contact Us</span>
  </nav>
</header>

<section class="hero" role="img" aria-label="Photo of rows of solar panels on green grass under a bright sky">
  <h1 class="hero-title">WHY PAY EXCESS FOR<br>YOUR ELECTRICITY?</h1>
  <p class="hero-sub">Save on electricity costs by switching to solar!</p>
  <p class="hero-copy">Did you know that you could install a solar system for a lower price than your current electricity costs! If you are paying for electricity, why not pay for greener, cleaner energy? It's that simple.</p>
  <span class="btn">Contact Us</span>

  <form class="quote">
    <div class="quote-head">Want A Free Quote?</div>
    <div class="field" style="left:21px;top:62px;width:200px">First Name<em>*</em><svg class="icon" style="margin-left:auto"><use href="#i-user"/></svg></div>
    <div class="field" style="left:228px;top:62px;width:195px">Last Name<em>*</em><svg class="icon" style="margin-left:auto"><use href="#i-user"/></svg></div>
    <div class="field" style="left:21px;top:107px;width:200px">Phone<em>*</em><svg class="icon" style="margin-left:auto"><use href="#i-phone"/></svg></div>
    <div class="field" style="left:228px;top:107px;width:195px">Email<em>*</em><svg class="icon" style="margin-left:auto"><use href="#i-mail"/></svg></div>
    <div class="field" style="left:21px;top:151px;width:402px">Please Enter A Valid Address<em>*</em><svg class="icon" style="margin-left:auto"><use href="#i-pin"/></svg></div>
    <div class="field" style="left:21px;top:196px;width:200px">I Am Interested In<em>*</em><svg class="icon" style="margin-left:auto;width:12px"><use href="#i-down"/></svg></div>
    <div class="field" style="left:228px;top:196px;width:195px">How Did You Find Us<em>*</em><svg class="icon" style="margin-left:auto;width:12px"><use href="#i-down"/></svg></div>
    <div class="field message" style="left:21px;top:241px;width:402px">Message<em style="margin-right:auto">*</em></div>
    <span class="btn">Submit</span>
  </form>
</section>

<section>
  <div class="about-visual" role="img" aria-label="Solar engineer in hard hat and safety vest holding a clipboard, set over a solar panel shape"></div>
  <div class="about">
    <h2 class="display"><span class="accent">ABOUT</span> KIVO4</h2>
    <p>Power bills have risen dramatically in Australia over the past decade, making energy bills amongst the highest utility expense for businesses and households alike.</p>
    <h3>That's where we come in!</h3>
    <p>We are a completely Australian Owned and Operated company that specialise in adapting the latest technologies to improve your energy efficiency and reduce costs.</p>
    <span class="btn">Read More</span>
  </div>
</section>

<section class="projects">
  <h2 class="display"><span class="accent">OUR</span> PROJECTS</h2>
  <span class="tab active">Residential Solar</span>
  <span class="tab plain">Commercial Solar</span>
  <div class="project p1" role="img" aria-label="Aerial photo of a large ground-mounted solar farm"><b>Reservoir 3</b><span>502 kW</span></div>
  <div class="project p2" role="img" aria-label="Photo of a warehouse roof covered in solar panels"><b>Freight Hub KTR</b><span>400 kW</span></div>
  <div class="project p3" role="img" aria-label="Photo of rooftop solar panel rows"><b>Brellon Safety</b><span>100 kW</span></div>
  <div class="project p4" role="img" aria-label="Photo of solar panels on a farm shed roof"><b>Ostrey Farms</b><span>99 kW</span></div>
  <div class="progress"><i></i></div>
  <span class="circle-btn" style="left:975px;top:528px;background:var(--white);color:#333"><svg class="icon"><use href="#i-left"/></svg></span>
  <span class="circle-btn" style="left:1025px;top:528px;background:var(--blue);color:var(--white)"><svg class="icon"><use href="#i-right"/></svg></span>
</section>

<section>
  <h2 class="display reviews-title"><span class="accent">CUSTOMER</span> REVIEWS</h2>
  <span class="side-arrow" style="left:95px"><svg class="icon"><use href="#i-arrow-l"/></svg></span>
  <article class="review" style="left:153px;top:2113px">
    <p>"Kivo4 are an awesome company with high levels of professionalism. Our panels were installed promptly with no issues. The team goes above and beyond to ensure their customers are happy. 100% recommended."</p>
    <footer><div><div class="who">Carla Mendes</div><div class="stars"><svg><use href="#i-star"/></svg><svg><use href="#i-star"/></svg><svg><use href="#i-star"/></svg><svg><use href="#i-star"/></svg><svg><use href="#i-star"/></svg></div></div><span class="dot"></span></footer>
  </article>
  <article class="review" style="left:472px;top:2078px">
    <p>"Very happy with the service. Kivo4 delivered what they promised, no hidden cost and very professional. Always replyand answer any questions. Thank you for the great service, I totally recommend to use Kivo4 for your solar."</p>
    <footer><div><div class="who">Tessa Lowe</div><div class="stars"><svg><use href="#i-star"/></svg><svg><use href="#i-star"/></svg><svg><use href="#i-star"/></svg><svg><use href="#i-star"/></svg><svg><use href="#i-star"/></svg></div></div><span class="dot"></span></footer>
  </article>
  <article class="review" style="left:789px;top:2113px">
    <p>"Very happy with the service. Kivo4 delivered what they promised, no hidden cost and very professional. Always replyand answer any questions. Thank you for the great service, I totally recommend to use Kivo4 for your solar."</p>
    <footer><div><div class="who">Tessa Lowe</div><div class="stars"><svg><use href="#i-star"/></svg><svg><use href="#i-star"/></svg><svg><use href="#i-star"/></svg><svg><use href="#i-star"/></svg><svg><use href="#i-star"/></svg></div></div><span class="dot"></span></footer>
  </article>
  <span class="side-arrow dark" style="left:1088px"><svg class="icon"><use href="#i-arrow-r"/></svg></span>
</section>

<section class="signup" role="img" aria-label="Dim photo of a city skyline at dusk">
  <h2 class="display"><span class="accent">SIGNUP</span> FOR THE<br>LATEST OFFERS</h2>
  <p style="top:257px">Get all the latest information on Special Discounts, Products &amp; Offers.</p>
  <div class="subscribe">
    <div class="input"><svg class="icon"><use href="#i-mail"/></svg>Enter Your Email Address</div>
    <div class="send">Subscribe</div>
  </div>
  <p style="top:374px">You can download our capability statement by clicking below:</p>
  <span class="btn">Download <svg class="icon"><use href="#i-download"/></svg></span>
</section>

<section class="strip" style="top:3173px">
  <div class="strip-label" style="width:142px">Our Clients</div>
  <svg class="icon chev"><use href="#i-left"/></svg>
  <div class="items">
    <span class="client-name">Brellon Safety</span>
    <span class="client-name">Northvale Fencing</span>
    <span class="client-name">Wentra Textiles</span>
    <span class="client-name">Coastline Post</span>
  </div>
  <svg class="icon chev"><use href="#i-right"/></svg>
</section>

<section class="strip" style="top:3305px">
  <div class="strip-label" style="width:282px">Accreditations &amp; Partners</div>
  <svg class="icon chev"><use href="#i-left"/></svg>
  <div class="items">
    <span class="badge" role="img" aria-label="Certified installer badge"></span>
    <span class="badge round" role="img" aria-label="Partner badge"></span>
    <span class="badge" role="img" aria-label="Approved solar retailer badge"></span>
    <span class="badge" style="width:120px" role="img" aria-label="Recycling partner badge"></span>
  </div>
  <svg class="icon chev"><use href="#i-right"/></svg>
</section>

<footer class="site-footer">
  <div class="brand"><span class="brand-mark"></span><span class="brand-name">Kivo4</span></div>
  <div class="brand-tag">Clean Power Solutions For Homes &amp; Business</div>
  <div class="socials"><span aria-label="Social profile"></span><span aria-label="Video channel"></span><span aria-label="Professional network"></span></div>

  <div class="col" style="left:368px">
    <h4>QUICK LINKS</h4>
    <ul class="links">
      <li>Heat Pumps</li><li>Solar</li><li>Capability Statement</li><li>LED</li><li>Service and Support</li><li>Contact Us</li>
    </ul>
  </div>

  <div class="col" style="left:565px">
    <h4>CONTACT DETAILS</h4>
    <div class="contact-item"><span class="ico"><svg class="icon"><use href="#i-clock"/></svg></span><div><b>Business Hours</b><span>9AM - 5PM</span></div></div>
    <div class="contact-item"><span class="ico"><svg class="icon"><use href="#i-phone"/></svg></span><div><b>Phone</b><span>(1300) 555-014</span></div></div>
    <div class="contact-item"><span class="ico"><svg class="icon"><use href="#i-mail"/></svg></span><div><b>Email</b><span>enquiries@kivo4.com.au</span></div></div>
  </div>

  <div class="col" style="left:830px">
    <h4>OFFICE LOCATIONS</h4>
    <div class="office"><svg class="icon"><use href="#i-pin"/></svg><span>12 Harlow Street Brennick<br>VIC 3040</span></div>
    <div class="office"><svg class="icon"><use href="#i-pin"/></svg><span>4C/21 Tamsin Drive Carwell<br>QLD 4218</span></div>
    <div class="office"><svg class="icon"><use href="#i-pin"/></svg><span>9 Foundry Court Ardlow<br>VIC 3490</span></div>
    <div class="office"><svg class="icon"><use href="#i-pin"/></svg><span>305/18 Quarry St, Perth<br>WA 6000</span></div>
    <div class="office"><svg class="icon"><use href="#i-pin"/></svg><span>2/64 Elswick Street Hobart<br>TAS 7000</span></div>
  </div>

  <div class="legal"><span>©2024 Kivo4. All Rights Reserved.</span><span>Privacy Policy &nbsp;|&nbsp; Installer Policy &nbsp;|&nbsp; FAQs</span></div>
</footer>
</body>
</html>
```